New Optometry Practice needs a Business Card

Need a business card for an Optometry practice called 'Marlow Vista Eyecare'. I would like to use designs that are friendly, fun and professional. Looking to incorporate glasses (see uploaded image). Not interested in design with an 'eye' in logo. Like green, blue, white as color choices..but open to your ideas. Back of card will be an appointment card as well as provide address, phone and email information.

Industry/Entity Type

Business

Contact Information for Business Card

Marlow Vista Eyecare
Dr. Petra Lindqvist, Optometrist (or O.D.)
4172 S Corbell Ave Wenatchee, WA 98736
PMarlowvistaeyecare.example

Colors
acd036
33b8a4
f68d4e
cfeae6
fee18a
cadf82

Requirements
Must have
• Appointment card on back with date/time of return for next exam

```html
<!DOCTYPE html>
<html lang="en">
<head>
<meta charset="utf-8">
<title>Marlow Vista Eyecare – Business Card</title>
<link rel="stylesheet" href="https://fonts.googleapis.com/css2?family=Open+Sans:ital,wght@0,400;0,600;0,700;1,400&display=swap">
<style>
  :root {
    --navy: #1f3580;
    --green: #4caf1a;
    --ink: #4a4a4a;
    --muted: #666666;
    --card: #ffffff;
    --stage: #e6e6e6;
    --rule: #9a9a9a;
  }
  * { box-sizing: border-box; margin: 0; padding: 0; }
  html, body { width: 1105px; height: 1200px; overflow: hidden; }
  body {
    background: var(--stage);
    font-family: "Open Sans", Arial, sans-serif;
    position: relative;
  }
  .card {
    position: absolute;
    left: 192px;
    width: 720px;
    height: 412px;
    background: var(--card);
    overflow: hidden;
  }
  .card--front { top: 146px; }
  .card--back { top: 604px; }

  .front-swoosh { position: absolute; inset: 0; }
  .brand-name {
    position: absolute;
    right: 40px;
    top: 90px;
    font-size: 27px;
    font-weight: 700;
    color: var(--navy);
    letter-spacing: -0.3px;
  }
  .contact { position: absolute; left: 38px; top: 228px; }
  .contact__name { font-size: 22px; font-weight: 600; color: var(--navy); line-height: 1.2; }
  .contact__role { font-size: 17px; font-weight: 700; color: var(--green); line-height: 1.3; margin-bottom: 12px; }
  .contact__line { font-size: 18px; color: var(--ink); line-height: 1.45; }
  .contact__web { font-size: 18px; color: var(--ink); margin-top: 10px; }

  .appt-title {
    position: absolute; top: 36px; left: 0; right: 0;
    text-align: center; font-size: 26px; font-weight: 600; color: var(--navy);
  }
  .appt-row {
    position: absolute; left: 34px; right: 34px;
    display: flex; align-items: baseline;
    font-size: 19px; color: var(--navy);
  }
  .appt-row--patient { top: 110px; }
  .appt-row--when { top: 184px; }
  .appt-row--days { top: 262px; justify-content: space-between; font-size: 17px; }
  .fill-line { border-bottom: 2px dotted var(--rule); height: 1px; align-self: flex-end; margin-bottom: 6px; }
  .fill-line--patient { width: 420px; margin-left: 6px; margin-right: 10px; }
  .fill-line--date { width: 272px; margin-left: 10px; margin-right: 24px; }
  .fill-line--time { width: 150px; margin-left: 6px; margin-right: 6px; }
  .appt-note-inline { color: var(--ink); font-size: 18px; }
  .ampm { font-size: 13px; }
  .day { display: flex; align-items: center; gap: 8px; }
  .day__box { width: 20px; height: 17px; border: 1.5px solid var(--ink); display: inline-block; }
  .appt-policy {
    position: absolute; left: 0; right: 0; top: 340px;
    text-align: center; font-size: 14px; font-style: italic; color: var(--muted); line-height: 1.5;
  }
</style>
</head>
<body>

<section class="card card--front" aria-label="Business card front">
  <svg class="front-swoosh" width="720" height="412" viewBox="0 0 720 412" aria-hidden="true">
    <path d="M0,0 H160 Q22,34 0,165 Z" fill="var(--navy)"/>
    <path d="M160,0 Q22,34 0,165 L0,178 Q30,40 176,0 Z" fill="var(--green)"/>
    <path d="M720,248 Q700,380 562,412 H720 Z" fill="var(--navy)"/>
    <path d="M720,248 Q700,380 562,412 L546,412 Q690,372 716,244 Z" fill="var(--green)"/>
  </svg>
  <div class="brand-name">Marlow Vista Eyecare</div>
  <div class="contact">
    <p class="contact__name">Dr. Petra Lindqvist</p>
    <p class="contact__role">Optometrist</p>
    <p class="contact__line">4172 S Corbell Ave</p>
    <p class="contact__line">Wenatchee, WA 98736</p>
    <p class="contact__web">PMarlowvistaeyecare.example</p>
  </div>
</section>

<section class="card card--back" aria-label="Appointment card back">
  <h2 class="appt-title">Next Appointment</h2>
  <div class="appt-row appt-row--patient">
    <span class="fill-line fill-line--patient" style="margin-left:0"></span>
    <span class="appt-note-inline">has an apppointment</span>
  </div>
  <div class="appt-row appt-row--when">
    <span>Date :</span><span class="fill-line fill-line--date"></span>
    <span>Time :</span><span class="fill-line fill-line--time"></span>
    <span class="ampm">AM/PM</span>
  </div>
  <div class="appt-row appt-row--days">
    <span class="day">Sun <i class="day__box"></i></span>
    <span class="day">Mon <i class="day__box"></i></span>
    <span class="day">Tue <i class="day__box"></i></span>
    <span class="day">Wed <i class="day__box"></i></span>
    <span class="day">Thu <i class="day__box"></i></span>
    <span class="day">Fri <i class="day__box"></i></span>
    <span class="day">Sat <i class="day__box"></i></span>
  </div>
  <p class="appt-policy">Please give me 24 hours notice if you are unable to keep your appointment or<br>a cancellation fee may be charged.</p>
</section>

</body>
</html>
```